New Zealand Marlborough Sauvignon Blanc wine packaging design

We need packaging design for our new wine brand, Dunmore Hale. The wine is a New Zealand Marlborough Sauvignon Blanc. We would like the packaging will portray elegance and style with an understated label. We are looking for a label that portrays the elegance of the French Riviera. The label should be round or pill shaped.
Updates

Industry/Entity Type

Wine

Font styles to use
Serif
Sans Serif

Requirements
Must have
• The words in order of importance: Dunmore Hale, Sauvignon Blanc, Marlborough, New Zealand. It should be fit to the bottle posted in the links
Nice to have
• a pill shape or circular shape
Should not have
• Illustrations of wine bottles, wine glasses, or grapes

```html
<!DOCTYPE html>
<html lang="en">
<head>
<meta charset="utf-8">
<title>Dunmore Hale – Sauvignon Blanc Label</title>
<link rel="stylesheet" href="https://fonts.googleapis.com/css2?family=Libre+Caslon+Display&family=Marcellus+SC&display=swap">
<style>
  :root {
    --backdrop: #e6e3e5;
    --label-black: #14110c;
    --gold: #d9a43a;
    --gold-deep: #8a5f17;
    --gold-light: #f0c560;
    --rule-white: #e9e4da;
  }
  html, body {
    margin: 0;
    padding: 0;
    width: 1200px;
    height: 1200px;
    overflow: hidden;
    background: var(--backdrop);
  }
  .canvas {
    position: relative;
    width: 1200px;
    height: 1200px;
  }
  .label {
    position: absolute;
    left: 320px;
    top: 190px;
    width: 560px;
    height: 820px;
  }
  .label-shape {
    position: absolute;
    inset: 0;
  }
  .label-text {
    position: absolute;
    inset: 0;
    text-align: center;
    color: var(--gold);
  }
  .brand-name {
    position: absolute;
    left: 0;
    right: 0;
    top: 318px;
    margin: 0;
    font-family: "Libre Caslon Display", serif;
    font-weight: 400;
    font-size: 98px;
    line-height: 0.98;
    letter-spacing: -1px;
    color: var(--gold);
  }
  .divider {
    position: absolute;
    left: 50%;
    top: 560px;
    width: 230px;
    height: 3px;
    margin-left: -115px;
    background: var(--rule-white);
  }
  .varietal {
    position: absolute;
    left: 0;
    right: 0;
    top: 600px;
    margin: 0;
    font-family: "Marcellus SC", sans-serif;
    font-size: 23px;
    line-height: 1.25;
    letter-spacing: 0.5px;
    color: var(--gold);
  }
</style>
</head>
<body>
  <main class="canvas">
    <section class="label">
      <svg class="label-shape" width="560" height="820" viewBox="0 0 560 820">
        <defs>
          <clipPath id="label-inner">
            <ellipse cx="280" cy="410" rx="266" ry="396"/>
          </clipPath>
          <linearGradient id="swirl-tones" x1="0" y1="0" x2="1" y2="1">
            <stop offset="0" stop-color="#c8922e"/>
            <stop offset="0.5" stop-color="#7a5316"/>
            <stop offset="1" stop-color="#3a2a10"/>
          </linearGradient>
          <linearGradient id="wave-tones" x1="0" y1="0" x2="0" y2="1">
            <stop offset="0" stop-color="#3a2a10"/>
            <stop offset="1" stop-color="#b8852a"/>
          </linearGradient>
        </defs>
        <ellipse class="label-body" cx="280" cy="410" rx="272" ry="402" fill="var(--label-black)" stroke="var(--gold)" stroke-width="9"/>
        <g clip-path="url(#label-inner)">
          <rect class="swirl-ornament" x="0" y="0" width="560" height="270" fill="url(#swirl-tones)" role="img" aria-label="Gold flowing swirl ornament across the top of the label"/>
          <rect class="wave-ornament" x="0" y="690" width="560" height="130" fill="url(#wave-tones)" role="img" aria-label="Gold wave line ornament along the bottom of the label"/>
        </g>
      </svg>
      <div class="label-text">
        <h1 class="brand-name">Dunmore<br>Hale</h1>
        <div class="divider"></div>
        <p class="varietal">Sauvignon Blanc,<br>Marlborough, New Zealand</p>
      </div>
    </section>
  </main>
</body>
</html>
```